Seeking funky, innovative business cards

I am looking to refresh our current business cards to something more engaging, visual and impactful. We are a management consultancy firm, see website (www.thornbury-partners.com.au). I've included our colour scheme, sample of the slides we use and our old business cards. We would like our cards to have icons. The card should display:- Name- Title- Mobile number- Address- Email address- Website - Company logo- Our purpose statement "We create the best places on earth to work"

Contact Information for Business Card

Radek Solvieri
Consultant
0491 627 358
Level 3, 218 Wexford Street, Melbourne 3000
radek@thornbury-partners.com.au
www.thornbury-partners.com.au

Purpose statement "we create the best places on earth to work"
LOGO available in google images

Font styles to use
Other font styles liked:
• Open Sans Light, Bebas Neue (open to other cool foints)

Colors
ffc214
5c5c5c
f5f5f5
fefefe

Requirements
Must have
• - Name
• - Title
• - Mobile number
• - Address
• - Email address
• - Website
• - Company logo
• - Our purpose statement "We create the best places on earth to work"
Nice to have
• - Icons
• - Colour (see our colour scheme"

```html
<!DOCTYPE html>
<html lang="en">
<head>
<meta charset="utf-8">
<title>Thornbury Partners – Business Card</title>
<link rel="stylesheet" href="https://fonts.googleapis.com/css2?family=Bebas+Neue&family=Open+Sans:wght@300;400&display=swap">
<style>
  :root {
    --backdrop: #2a2a2a;
    --card: #444647;
    --accent: #ffc214;
    --white: #fefefe;
    --soft: #f5f5f5;
    --muted: #b8b8b8;
    --divider: #d8d8d8;
    --icon-ink: #444647;
  }
  * { box-sizing: border-box; margin: 0; padding: 0; }
  html, body {
    width: 1200px; height: 895px; overflow: hidden;
    background: var(--backdrop);
  }
  .stage {
    position: relative; width: 1200px; height: 895px;
    display: flex; align-items: center; justify-content: center; gap: 24px;
  }
  .card {
    position: relative; width: 572px; height: 340px; flex: none;
    background: var(--card);
    border-radius: 18px;
    border-bottom: 5px solid var(--accent);
    box-shadow: 0 14px 30px rgba(0,0,0,.45);
    overflow: hidden;
    color: var(--white);
    font-family: "Open Sans", sans-serif;
    font-weight: 300;
  }

  /* Front */
  .card--front {
    display: flex; flex-direction: column; align-items: center; justify-content: center;
  }
  .brand { display: flex; align-items: center; gap: 14px; }
  .brand__dot { width: 18px; height: 18px; border-radius: 50%; background: var(--accent); }
  .brand__name { font-size: 46px; font-weight: 300; letter-spacing: .5px; color: var(--white); white-space: nowrap; }
  .tagline { margin-top: 24px; font-size: 17px; font-weight: 400; letter-spacing: .4px; color: var(--soft); }
  .purpose { margin-top: 8px; font-size: 13px; font-weight: 300; letter-spacing: .3px; color: var(--muted); }

  /* Back */
  .identity {
    position: absolute; left: 32px; top: 110px;
    display: flex; align-items: stretch;
  }
  .person { display: flex; flex-direction: column; justify-content: center; padding-right: 14px; }
  .person__name {
    font-family: "Bebas Neue", sans-serif; font-weight: 400; font-size: 40px; line-height: 1;
    color: var(--white); letter-spacing: .5px; white-space: nowrap;
  }
  .person__title { font-size: 15px; color: var(--accent); text-align: right; margin-top: 2px; }
  .rule { width: 1.5px; background: var(--divider); margin: 2px 0; flex: none; }
  .contacts { list-style: none; padding-left: 12px; display: flex; flex-direction: column; gap: 6px; justify-content: center; }
  .contact { display: flex; align-items: center; gap: 7px; font-size: 11.5px; font-weight: 400; color: var(--soft); white-space: nowrap; }
  .contact__icon {
    width: 18px; height: 18px; border-radius: 50%; background: var(--accent);
    display: flex; align-items: center; justify-content: center; flex: none;
  }
  .contact__icon svg { width: 11px; height: 11px; }
  .hl { color: var(--accent); }
  .address {
    position: absolute; right: 34px; bottom: 40px;
    font-size: 14px; font-weight: 400; color: var(--soft); letter-spacing: .3px; white-space: nowrap;
  }
</style>
</head>
<body>
<main class="stage">
  <section class="card card--front" aria-label="Card front">
    <div class="brand">
      <span class="brand__dot"></span>
      <span class="brand__name">Thornbury Partners</span>
    </div>
    <p class="tagline">Strategy. People. Impact.</p>
    <p class="purpose">We create the best places on earth to work</p>
  </section>

  <section class="card card--back" aria-label="Card back">
    <div class="identity">
      <div class="person">
        <h1 class="person__name">Radek Solvieri</h1>
        <p class="person__title">Consultant</p>
      </div>
      <span class="rule"></span>
      <ul class="contacts">
        <li class="contact">
          <span class="contact__icon">
            <svg viewBox="0 0 12 12"><rect x="3" y="1" width="6" height="10" rx="1.2" fill="none" stroke="var(--icon-ink)" stroke-width="1.4"/><circle cx="6" cy="9" r=".8" fill="var(--icon-ink)"/></svg>
          </span>
          0491 627 358
        </li>
        <li class="contact">
          <span class="contact__icon">
            <svg viewBox="0 0 12 12"><rect x="1.5" y="3" width="9" height="6.5" rx=".8" fill="none" stroke="var(--icon-ink)" stroke-width="1.3"/><path d="M1.8 3.4 6 6.6l4.2-3.2" fill="none" stroke="var(--icon-ink)" stroke-width="1.3"/></svg>
          </span>
          <span>radek@<span class="hl">thornbury-partners</span>.com.au</span>
        </li>
        <li class="contact">
          <span class="contact__icon">
            <svg viewBox="0 0 12 12"><circle cx="6" cy="6" r="4.4" fill="none" stroke="var(--icon-ink)" stroke-width="1.3"/><path d="M1.6 6h8.8M6 1.6c-2.2 2.4-2.2 6.4 0 8.8M6 1.6c2.2 2.4 2.2 6.4 0 8.8" fill="none" stroke="var(--icon-ink)" stroke-width="1"/></svg>
          </span>
          <span>www.<span class="hl">thornbury-partners</span>.com.au</span>
        </li>
      </ul>
    </div>
    <p class="address">Level 3, 218 Wexford Street, Melbourne 3000</p>
  </section>
</main>
</body>
</html>
```